ad for food show brochure

Need to clean up this concept sketch. We are selling food at a festival but the concept isn't quite named. We're looking to create a buzz and have people sign up to be kept apprised of the progress of the chain ... or the first store. The website at the bottom is just for filler, we can add that before ad goes to print. We're not married to this text so if you come up with something better, great. also may want to have a blank @ line for twitter feed and another line for FB page.
The concept is for a Vegan Fast Food place but I need to focus more on the middle of the road diners, we'll get the vegans to come and staunch carnivores won't ever come so it's the middle of the road folks we're after. The slant and speed lines were my attempt to show speed.
Thanks.
This ad is a 5/5 x 2.125 space in the festival brochure. Need this asap.
I also think this needs to be b&w so lets go with that. Just found out COLOR is ok.
That last word in the sketch is not whose but WHERE?
The last word is WHERE not whose. Thanks
We either need to add the word Vegan in the top of the ad or add it in the sentence about all that is vegan and good in the worl.
The ad can be in color. Just to clarify, the word Vegan should be o e of the questions on top. Eithe as part of another question ... 'Vegan fast food?' Or as its own line or bubble.
- pdf file so I can change the website address.

```html
<!DOCTYPE html>
<html lang="en">
<head>
<meta charset="utf-8">
<title>Vegan Fast Food – Coming Soon to NYC</title>
<link rel="stylesheet" href="https://fonts.googleapis.com/css2?family=Bebas+Neue&family=Luckiest+Guy&family=Montserrat:wght@300;600;700&display=swap">
<style>
  :root {
    --orange: #f7901e;
    --green: #8cc63f;
    --green-deep: #5e8c31;
    --white: #ffffff;
  }
  * { margin: 0; padding: 0; box-sizing: border-box; }
  html, body { width: 1200px; height: 3103px; overflow: hidden; background: var(--white); }
  .ad { position: relative; width: 1200px; height: 3103px; background: var(--white); overflow: hidden; }

  .veg-row .veg { position: absolute; top: 30px; height: 360px; border-radius: 40%; }
  .veg-turnip   { left: 52px;  width: 232px; background: radial-gradient(circle at 50% 60%, #d9efbd, #b6dd86); }
  .veg-carrot   { left: 388px; width: 194px; background: linear-gradient(160deg, #c8e7a0, #e9f5d8); }
  .veg-eggplant { left: 608px; width: 245px; background: radial-gradient(circle at 45% 55%, #dff0c8, #b3da80); }
  .veg-corn     { left: 918px; width: 220px; background: linear-gradient(200deg, #bfe291, #e6f4d3); }

  .headline {
    position: absolute; left: 0; width: 1200px;
    color: var(--orange); line-height: 1; text-align: center; white-space: nowrap;
  }
  .headline-big {
    font-family: 'Bebas Neue', 'Oswald', sans-serif;
    font-size: 234px; letter-spacing: 4px;
    transform: scaleX(1.17); transform-origin: center;
  }
  .headline-small {
    font-family: 'Montserrat', sans-serif; font-weight: 700;
    font-size: 90px; letter-spacing: 1px;
  }
  .line-1 { top: 470px; }
  .line-2 { top: 676px; }
  .line-3 { top: 918px; }
  .line-4 { top: 991px; }

  .divider { position: absolute; left: 31px; top: 1250px; width: 1130px; height: 5px; background: var(--green-deep); }

  .tagline {
    position: absolute; left: 34px; top: 1262px; width: 1130px;
    font-family: 'Montserrat', sans-serif; font-weight: 600;
    font-size: 148px; line-height: 200px; letter-spacing: -2px;
    color: var(--green); white-space: nowrap;
  }

  .where {
    position: absolute; left: 0; top: 2085px; width: 1200px;
    font-family: 'Luckiest Guy', cursive;
    font-size: 262px; line-height: 1; text-align: center;
    color: var(--green); -webkit-text-stroke: 7px var(--green-deep);
    letter-spacing: 8px; white-space: nowrap;
  }

  .website {
    position: absolute; left: 0; top: 2418px; width: 1200px;
    font-family: 'Montserrat', sans-serif; font-weight: 700;
    font-size: 52px; line-height: 64px; letter-spacing: 1px; text-align: center;
    color: var(--orange); white-space: nowrap;
  }

  .promo-band { position: absolute; left: 0; top: 2565px; width: 1200px; height: 538px; background: var(--orange); }
  .promo-title {
    position: absolute; left: 36px; top: 2628px;
    font-family: 'Bebas Neue', 'Oswald', sans-serif; font-size: 192px; line-height: 1;
    color: var(--white); letter-spacing: 4px; white-space: nowrap;
  }
  .promo-copy {
    position: absolute; left: 36px; top: 2820px;
    font-family: 'Montserrat', sans-serif; font-weight: 300;
    font-size: 92px; line-height: 129px; color: var(--white);
    letter-spacing: -1px; white-space: nowrap;
  }
  .promo-copy strong { font-weight: 700; letter-spacing: -2px; }
  .drumstick-art {
    position: absolute; left: 985px; top: 2640px; width: 170px; height: 430px;
    border-radius: 50% 50% 40% 40%;
    background: linear-gradient(180deg, #fbb45e, #f9a443);
  }
</style>
</head>
<body>
<main class="ad">
  <div class="veg-row">
    <div class="veg veg-turnip" role="img" aria-label="Line drawing of a turnip"></div>
    <div class="veg veg-carrot" role="img" aria-label="Line drawing of a carrot"></div>
    <div class="veg veg-eggplant" role="img" aria-label="Line drawing of an eggplant"></div>
    <div class="veg veg-corn" role="img" aria-label="Line drawing of an ear of corn"></div>
  </div>

  <h1 class="headline headline-big line-1">VEGAN FAST</h1>
  <p class="headline headline-big line-2">FOOD? YEP!</p>
  <p class="headline headline-small line-3">COMING SOON? YEP!</p>
  <p class="headline headline-big line-4">IN NYC? YEP!</p>

  <div class="divider"></div>

  <p class="tagline">In the name of<br>all that is good<br>in the World...</p>

  <p class="where">WHERE?</p>

  <p class="website">WWW.GREENLANE-QUICKBITES.COM</p>

  <section class="promo-band"></section>
  <p class="promo-title">UNTIL THEN...</p>
  <p class="promo-copy">Enjoy our vegan<br><strong>GROVESTIX</strong> today!</p>
  <div class="drumstick-art" role="img" aria-label="Line drawing of a drumstick with a leaf"></div>
</main>
</body>
</html>
```